Drug safety monitoring company requires a new corporate website

We are an outsourcing partner to large and small companies within the pharmaceutical industry. Our current website www.quorvanta.co.uk has not been updated in a long time. We want a new web site that is responsive and modern but with a clearly corporate and professional feel. We want a design based on a 12 column grid system (mobile and desktop version). We want to use a new, modern font (not the standard web fonts) - we will purchase as required. Content can be used as is from the current website. Red and white are the corporate colours, so a palate should be developed to match. We do not need as much red as is in the current website. New icons (preferably in svg format) would be great. We can also purchase new images from Framly (or other) as required. We would prefer submissions in Sketch if possible.

Target Market(s)

Pharmaceutical companies

Number of Pages Required

1 page

Font styles to use
Sans Serif

Colors
ec1f27
ffffff

Requirements
Must have
• Design based on 12 column grid system.
Responsive design (i.e. require a mobile and desktop version).
How should the menu look between desktop and mobile?
A coherent colour palete.
Content to come from the existing website: www.quorvanta.co.uk
How should links be styled?
How should headings, sub-headings, paragraphs be styled?
Nice to have
• Custom developed icons (these are along the bottom of the page on the existing website: Medical Information; Pharmacovigilance; Literature Monitoring; Training).
New imagery (the images on the current website are dated).
Submission ideally as Sketch files (but we are okay with photoshop too).
A new, modern, non-standard font.
Not so much red in the design.
If we had buttons on the website, how should they be styled?
If we had a form on the website, how should the fields be styled?

```html
<!DOCTYPE html>
<html lang="en">
<head>
<meta charset="utf-8">
<title>Quorvanta Pharmacovigilance</title>
<link rel="stylesheet" href="https://fonts.googleapis.com/css2?family=Figtree:wght@400;500;600;700;800&display=swap">
<style>
:root{
  --red:#ec1f27;
  --white:#ffffff;
  --ink:#111111;
  --text:#222222;
  --muted:#444444;
  --soft:#f5f5f5;
  --band:#d4d4d4;
}
*{box-sizing:border-box;margin:0;padding:0}
html,body{width:1200px;height:2529px;overflow:hidden}
body{font-family:"Figtree",sans-serif;color:var(--text);background:var(--white);position:relative}

/* header */
.site-header{position:absolute;left:0;top:0;width:1200px;height:100px;background:var(--white)}
.brand{position:absolute;left:113px;top:30px;display:flex;align-items:center;gap:10px}
.brand-mark{width:16px;height:16px;background:var(--red)}
.brand-name{font-weight:700;font-size:22px;letter-spacing:4px;color:var(--red)}
.main-nav{position:absolute;left:369px;top:41px;display:flex;gap:20px;font-size:14px;font-weight:500;color:var(--ink)}
.main-nav a{color:inherit;text-decoration:none}
.call{position:absolute;left:898px;top:28px;display:flex;align-items:center;gap:10px}
.call-label{font-size:12px;letter-spacing:2.4px;font-weight:500;color:var(--ink)}
.call-number{font-size:20px;font-weight:700;color:var(--red);margin-top:1px}

/* hero */
.hero{position:absolute;left:0;top:100px;width:1200px;height:583px;
  background:linear-gradient(100deg,#eef2f6 0%,#e6edf3 38%,#c9d8e6 62%,#9fb7cd 82%,#b8cbdc 100%)}
.hero-title{position:absolute;left:112px;top:160px;font-size:37px;font-weight:700;line-height:50px;color:var(--ink)}
.hero-sub{position:absolute;left:112px;top:270px;font-size:24px;line-height:31px;color:var(--ink);font-weight:400}
.btn{display:inline-flex;align-items:center;justify-content:center;background:var(--red);color:var(--white);
  font-weight:800;font-size:14px;border-radius:25px;width:150px;height:50px;text-decoration:none;letter-spacing:-.2px}
.hero .btn{position:absolute;left:112px;top:365px}

/* welcome */
.welcome{position:absolute;left:0;top:733px;width:1200px;text-align:center}
.welcome h2{font-size:37px;font-weight:700;line-height:49px;color:var(--ink)}
.welcome h2 span{color:var(--red);display:block}
.welcome p{width:840px;margin:26px auto 0;font-size:14px;line-height:25px;color:var(--text)}

/* functions */
.functions h2{position:absolute;left:112px;top:1046px;font-size:38px;font-weight:700;color:var(--ink)}
.functions .copy{position:absolute;left:112px;top:1116px;width:470px;font-size:14px;line-height:25px}
.functions .copy p+p{margin-top:25px}
.photo{position:absolute;box-shadow:0 10px 30px rgba(0,0,0,.15)}
.frame{position:absolute;left:722px;top:1133px;width:272px;height:270px;border:7px solid var(--red)}

/* services */
.services{position:absolute;left:0;top:1543px;width:1200px;height:432px;background:var(--soft)}
.services h2{position:absolute;left:0;width:1200px;top:68px;text-align:center;font-size:38px;font-weight:700;color:var(--ink)}
.card{position:absolute;top:143px;width:225px;height:216px;background:var(--white);text-align:center}
.card .icon{width:84px;height:84px;border-radius:50%;background:var(--red);margin:17px auto 0;display:flex;align-items:center;justify-content:center}
.card h3{font-size:19px;font-weight:700;color:var(--ink);margin-top:14px}
.card p{font-size:13px;line-height:20px;color:var(--muted);margin:8px 14px 0}

/* brochure */
.brochure{position:absolute;left:0;top:1975px;width:1200px;height:475px;background:var(--band)}
.brochure-visual{position:absolute;left:158px;top:60px;width:413px;height:345px;
  background:linear-gradient(90deg,#ececec 0%,#ececec 49%,#ffffff 49%,#f7f7f7 100%)}
.brochure h2{position:absolute;left:639px;top:145px;font-size:38px;font-weight:700;line-height:49px;color:var(--ink)}
.brochure .btn{position:absolute;left:640px;top:267px}

/* footer */
.site-footer{position:absolute;left:0;top:2450px;width:1200px;height:79px;text-align:center;font-size:14px;line-height:79px;color:var(--ink)}
</style>
</head>
<body>

<header class="site-header">
  <div class="brand"><span class="brand-mark"></span><span class="brand-name">QUORVANTA</span></div>
  <nav class="main-nav">
    <a href="#">HOME</a><a href="#">ABOUT US</a><a href="#">QPPV</a><a href="#">OUR SERVICES</a><a href="#">CONTACT US</a><a href="#">CLIENT</a>
  </nav>
  <div class="call">
    <svg width="42" height="42" viewBox="0 0 42 42" aria-hidden="true">
      <path d="M10 5l6 8-4 4c2 5 6 9 11 11l4-4 8 6-4 6c-13-1-26-14-27-27z" fill="var(--red)"/>
      <path d="M26 6a10 10 0 0 1 10 10M26 1a15 15 0 0 1 15 15M26 11a5 5 0 0 1 5 5" stroke="var(--red)" stroke-width="2.5" fill="none" stroke-linecap="round"/>
    </svg>
    <div><div class="call-label">CALL US TODAY!</div><div class="call-number">0330 555 0142</div></div>
  </div>
</header>

<section class="hero" role="img" aria-label="Clinician in a white coat stacking wooden blocks printed with medical symbols">
  <h1 class="hero-title">At Quorvanta We Ensure<br>That Your Business</h1>
  <p class="hero-sub">has the best Pharmacovigilance<br>support in the industry</p>
  <a class="btn" href="#">CONTACT US</a>
</section>

<section class="welcome">
  <h2>Welcome to The <span>Quorvanta Pharmacovigilance</span></h2>
  <p>We are an outsourcing partner to large and small companies within the pharmaceutical industry. Our range of services is tailored to suit each of our client’s needs and cover both human and veterinary medicinal products. Pharmacovigilance is defined by WHO as ‘The science and activities relating to the detection, assessment, understanding and prevention of adverse effects or any other drug-related problems’. The process is one of managing risk associated with medicinal products, in an effort to promote their safe and effective use by prescribers and patients.</p>
</section>

<section class="functions">
  <h2>Our Primary Functions</h2>
  <div class="copy">
    <p>are EU QPPV and related pharmacovigilance services to assist and support Marketing Authorisation Holders (MAH), of pharmaceutical product licences, in their efforts to remain compliant with EU regulatory requirements (Regulation 1235/2010 and Directive 2010/84/EU) the deadline for which implementing ended on 21 July 2012.</p>
    <p>The regulatory environment is an ever-changing and evolving one. Legislation is global and the management of this process is complex, requiring a strong relationship between Marketing Authorisation Holders and their QPPV. Good Pharmacovigilance Practice is dependant on a sound understanding of the key principles of this science and the ability to apply this knowledge competently on behalf of the client.</p>
  </div>
  <div class="frame"></div>
  <div class="photo" role="img" aria-label="Assorted red and white capsules spilling from a bottle" style="left:595px;top:1033px;width:348px;height:305px;background:linear-gradient(135deg,#9db4cc,#6f8aa8 60%,#1f3f8a)"></div>
  <div class="photo" role="img" aria-label="Businessman touching a digital interface of connected icons" style="left:802px;top:1233px;width:266px;height:234px;background:linear-gradient(135deg,#3f4650,#6f7d8c 55%,#a9bccd)"></div>
</section>

<section class="services">
  <h2>Our Services</h2>
  <div class="card" style="left:112px">
    <div class="icon"><svg width="44" height="44" viewBox="0 0 44 44" fill="none" stroke="#fff" stroke-width="2"><rect x="8" y="10" width="22" height="28" rx="2"/><path d="M14 10V6h22v28h-6"/><circle cx="19" cy="20" r="6"/><path d="M19 17v6M16 20h6M12 30h14M12 34h10"/></svg></div>
    <h3>Medical Information</h3>
    <p>Professional enquiry handling to support the safe and effective use of your products</p>
  </div>
  <div class="card" style="left:362px">
    <div class="icon"><svg width="44" height="44" viewBox="0 0 44 44" fill="none" stroke="#fff" stroke-width="2"><rect x="12" y="5" width="16" height="6"/><path d="M10 11h20v26H10z"/><path d="M20 19v8M16 23h8"/><rect x="24" y="26" width="16" height="9" rx="4.5" transform="rotate(-30 32 30)"/></svg></div>
    <h3>Pharmacovigilance</h3>
    <p>Ease the regulatory burden and keep compliant with current pharmacovigilance legislation.</p>
  </div>
  <div class="card" style="left:612px">
    <div class="icon"><svg width="44" height="44" viewBox="0 0 44 44" fill="none" stroke="#fff" stroke-width="2"><rect x="6" y="6" width="28" height="24" rx="2"/><path d="M10 24l6-7 5 4 6-8"/><circle cx="28" cy="28" r="6"/><path d="M32 32l7 7"/></svg></div>
    <h3>Literature Monitoring</h3>
    <p>Product safety through surveillance of published articles and case reports.</p>
  </div>
  <div class="card" style="left:862px">
    <div class="icon"><svg width="44" height="44" viewBox="0 0 44 44" fill="none" stroke="#fff" stroke-width="2"><rect x="16" y="6" width="22" height="18" rx="1"/><path d="M20 12h14M20 17h10"/><circle cx="10" cy="14" r="4"/><path d="M4 38V24a4 4 0 0 1 4-4h6l8-4M10 38V28M16 38V24"/></svg></div>
    <h3>Training</h3>
    <p>Professional enquiry handling to support the safe and effective use of your products</p>
  </div>
</section>

<section class="brochure">
  <div class="brochure-visual" role="img" aria-label="Open company brochure"></div>
  <h2>Download Our<br>Company Brochure</h2>
  <a class="btn" href="#">LEARN MORE</a>
</section>

<footer class="site-footer">Copyright © 2020 Quorvanta Ltd (Registered in England &amp; Wales : 09184726)</footer>

</body>
</html>
```